Electronic Music Artist needs an Album Cover

DRELL is an electronic musician from Boston, Massachusetts. He needs an album cover that captures the essence of his music. The album is called Lanterns, which represents his experiences growing up, positive and negative. He would like to see designs that involves color and creativity. Attached are some examples of artworks that DRELL likes. He also included a few of his original photos (optional to use. Using a photo will not effect his final decision!), and his logo.

Colors

Designer to choose colors to be used in the design.

Requirements
Must have
• My project must have the text "Lanterns" and "DRELL", and the logo (attached in the files). The logo should not be the main subject of the artwork. Everything must look aesthetically pleasing.
Nice to have
• It would be nice to have some sort of creative graphic design (see example album covers for reference). Also, in one of the references, there is a column on the left hand side with some text in it. That could be cool to include, but without the asian text.
Should not have
• The project should not have any other language besides English.

```html
<!DOCTYPE html>
<html lang="en">
<head>
<meta charset="utf-8">
<title>DRELL — Lanterns</title>
<link href="https://fonts.googleapis.com/css2?family=Montserrat:wght@300;800&display=swap" rel="stylesheet">
<style>
  :root {
    --spine-green: #009148;
    --outline: #0d1a2b;
    --deep-blue: #1c4596;
    --sky-blue: #00b2dd;
    --mid-blue: #1d86c9;
    --violet: #6e4595;
    --leaf-green: #7bbb55;
    --amber: #f3b21a;
    --sun-yellow: #fdd816;
    --ink: #141414;
  }
  html, body {
    margin: 0;
    padding: 0;
    width: 1200px;
    height: 1200px;
    overflow: hidden;
    background: #ffffff;
  }
  .cover {
    position: relative;
    width: 1200px;
    height: 1200px;
    overflow: hidden;
    font-family: "Montserrat", sans-serif;
  }
  .spine {
    position: absolute;
    left: 0;
    top: 0;
    width: 179px;
    height: 1200px;
    background: var(--spine-green);
    border-right: 2px solid var(--outline);
    box-sizing: border-box;
  }
  .artwork {
    position: absolute;
    left: 179px;
    top: 0;
    width: 1021px;
    height: 1200px;
    background:
      radial-gradient(circle at 92% 80%, var(--sun-yellow) 0%, var(--amber) 18%, rgba(243,178,26,0) 34%),
      radial-gradient(circle at 70% 12%, var(--violet) 0%, rgba(110,69,149,0) 30%),
      radial-gradient(circle at 30% 45%, var(--leaf-green) 0%, rgba(123,187,85,0) 22%),
      radial-gradient(circle at 20% 85%, var(--deep-blue) 0%, rgba(28,69,150,0) 35%),
      linear-gradient(135deg, var(--mid-blue) 0%, var(--sky-blue) 45%, var(--deep-blue) 100%);
    border-top: 3px solid var(--outline);
    box-sizing: border-box;
  }
  .credits {
    position: absolute;
    right: 106px;
    top: 676px;
    text-align: right;
    color: var(--ink);
  }
  .artist-mark {
    display: block;
    font-weight: 800;
    font-size: 40px;
    line-height: 1;
    letter-spacing: 1px;
    margin-bottom: 46px;
  }
  .artist-name {
    display: block;
    font-weight: 800;
    font-size: 27px;
    line-height: 1;
    letter-spacing: 0.5px;
  }
  .album-title {
    display: block;
    font-weight: 300;
    font-size: 30px;
    line-height: 1.15;
    letter-spacing: 0.5px;
    text-transform: uppercase;
  }
</style>
</head>
<body>
  <main class="cover">
    <aside class="spine"></aside>
    <div class="artwork" role="img" aria-label="Flowing stained-glass style illustration of two abstract figures in blue, violet, green and amber curves with swirling loops"></div>
    <div class="credits">
      <span class="artist-mark">DRELL</span>
      <span class="artist-name">DRELL</span>
      <span class="album-title">Lanterns</span>
    </div>
  </main>
</body>
</html>
```